Real estate team needs a poster design to promote Free Listing competition

Need a poster design to promote a free listing competition we have about to get underway. It will run from Jan 1,2014 - June 30, 2014 (yes, I'm running late getting this piece organized :-) )! To win a free listing from us, videos need to be submitted that show why they should win the competition and get a free listing from us. It is voted on by the general public on our website. Website is currently being modified to incorporate this so it is not 'live' yet. Our team is KTHomesDirect.com.

I'd like to see designs with blue tones as a focus (our logo and branding is in blue), with some other complementary (and wow) colors incorporated. I'd like to have some depth to the poster, and like what I see with 3D text. Since the competition is about clients submitting videos a movie poster style might be appropriate.

It should be eyecatching and want people to investigate more. A catchy phrase could be 'Lights, Camera, SOLD'. Perhaps this in text in 3D, with lights shining on it, and depth behind it...?? The explanation of the contest could be 'Win the listing services of an exceptional, progressive and dynamic real estate team - a winning video is all we need'.

It should include a pointer for more information to FreeListing.KTHomesDirect.com and the date of Jan 1-June 30, 2014, or email FreeListing@KTHomesDirect.com

We would also use this same design on a A4 size postcard, and print ad.
Updates

Hi folks,

I've just uploaded a zip file of a few iterations of our team logo.  Please note though that the .eps files that I have included have the wrong blue in them.  The correct blue (which is shown in some of the .svg, jpg,.png files) is R 73, G102, B151.

Thank you all very much... looking forward to seeing what you will come up with :-)
Roz

Hello,

thank you for the entries so far.  I am liking what I am seeing.

A few thoughts.  I like the emphasis on the words 'Lights, Camera, SOLD' that I am seeing.  I am liking the incorporation of movie lighting and movie cameras as well. I also like the depth, and 3D components that I've seen in some. 

I've seen designs which have no visual of homes for sale, and some which have stock photos of homes for sale, but am now thinking that we do need some visual representation of the fact that the team sell houses.  When there are no houses in the posters then you actually have to read the text to see that we sell houses if you don't know us, but we want people to get the fact that we sell real estate immediately from first glance... so we should somehow get some visuals of houses in here also.

Some nice homes which have Images that I own, and also videos that I own, are at www.62Orcutt.com, www.8Priscot.com, www41Hartwell.com ...perhaps something of one of these can be incorporated in to give some visuals?

Thanks so much for your efforts
Roz

Hey folks,
I've just uploaded some more photos. 
With some designs that are featuring photos of houses that we have sold very prominently we perhaps should use photos of my own home instead because I am concerned about the new owners protesting about including photos of their home in the poster.  If the photo is small, or transparent it is not as much of a concern, but where it is prominent it may be more appropriate to use a photo/s where we know the owner won't complain (me :-) ).
I also added a couple of photos of the team in case you wanted to use photos of the team in your design... it is not necessary, but I'd prefer the team versus anonymous people :-)
Thanks again for all submissions... I'm so pleased with what we are getting submitted...!
Thanks
Roz 

Target Market(s)

Homeowners aged 30-55+ who are comfortable with technology. Our main demographic are well educated and have professional occupations.

Industry/Entity Type

Progressive

Requirements
Must have
• It should include a link for more information of FreeListing.KTHomesDirect.com and the date of Jan 1-June 30, 2014. Or to email FreeListing@KTHomesDirect.com
Must have our logo incorporated somewhere on the poster.
Nice to have
• Like to show depth in the poster...perhaps a background, then the 3D words of 'Lights, Camera, SOLD', and perhaps a couple of lights and movie camera in the foreground? We're open but in posters that I have seen while looking for ideas I like the ones with some depth to them.
Like blues, and blue tones with some other colors that 'pop'.
Eyecatching.
Would be great to have the explanation of the contest incorporated somewhere on the poster so that people get the idea immediately of what its all about 'Win the listing services of an exceptional, progressive and dynamic real estate team - a winning video is all we need'

```html
<!DOCTYPE html>
<html lang="en">
<head>
<meta charset="utf-8">
<title>Lights Camera Sold – Free Listing Competition</title>
<link rel="stylesheet" href="https://fonts.googleapis.com/css2?family=Francois+One&family=Permanent+Marker&family=Tinos:wght@700&family=Arimo&display=swap">
<style>
  :root {
    --page-bg: #ecebe8;
    --poster-dark: #05080d;
    --poster-navy: #0c1a2b;
    --light-blue: #5fa9d6;
    --pale-blue: #bfe3f5;
    --brand-blue: #496697;
    --lens-gold: #b27a3a;
    --lens-amber: #e0902f;
    --text-white: #ffffff;
    --text-silver: #d9dde2;
    --rule-grey: #7c8590;
  }
  * { margin: 0; padding: 0; box-sizing: border-box; }
  html, body { width: 1026px; height: 1200px; overflow: hidden; background: var(--page-bg); }
  .poster {
    position: absolute; left: 118px; top: 20px; width: 790px; height: 1160px;
    background: linear-gradient(160deg, var(--poster-navy) 0%, var(--poster-dark) 55%, #03050a 100%);
    overflow: hidden; font-family: "Arimo", Arial, sans-serif; color: var(--text-white);
  }
  .hero-art {
    position: absolute; left: 0; top: 0; width: 790px; height: 760px;
    background:
      radial-gradient(circle at 510px 440px, var(--lens-amber) 0%, #7a3d16 14%, #2a1a10 26%, transparent 40%),
      radial-gradient(circle at 165px 560px, #8a5a3a 0%, #3b2418 10%, transparent 18%),
      radial-gradient(ellipse at 760px 140px, var(--pale-blue) 0%, var(--light-blue) 18%, transparent 45%),
      linear-gradient(200deg, #1b3550 0%, #0a121d 45%, transparent 80%);
  }
  .light-ray {
    position: absolute; width: 1200px; height: 70px; left: -60px;
    background: linear-gradient(90deg, transparent 0%, rgba(120,190,230,.35) 40%, rgba(200,235,255,.55) 80%, transparent 100%);
    transform: rotate(-30deg); transform-origin: left center; filter: blur(6px);
  }
  .ray-one { top: 900px; }
  .ray-two { top: 1000px; height: 40px; opacity: .7; }
  .dates { position: absolute; left: 39px; top: 48px; font-size: 30px; color: var(--text-white); }
  .headline {
    position: absolute; left: 0; top: 0; width: 790px; height: 760px;
    font-family: "Francois One", "Arial Black", sans-serif; text-transform: uppercase;
  }
  .headline span {
    position: absolute; transform: translate(-50%, -50%) rotate(-22deg);
    font-size: 104px; letter-spacing: 4px; line-height: 1; white-space: nowrap;
    color: var(--text-silver);
    text-shadow: 0 2px 0 #9aa1a8, 0 4px 0 #6f767d, 0 8px 14px rgba(0,0,0,.7);
  }
  .headline .word-lights { left: 457px; top: 311px; }
  .headline .word-camera { left: 466px; top: 436px; }
  .headline .word-sold { left: 502px; top: 556px; }
  .competition-title {
    position: absolute; left: 62px; top: 744px; font-size: 36px; color: var(--text-silver);
  }
  .competition-rule {
    position: absolute; left: 39px; top: 797px; width: 623px; height: 2px;
    background: linear-gradient(90deg, transparent, var(--rule-grey) 15%, var(--rule-grey) 80%, transparent);
  }
  .pitch {
    position: absolute; right: 39px; top: 808px; width: 720px; text-align: right;
    font-family: "Permanent Marker", cursive; font-size: 24px; line-height: 30px; color: var(--text-white);
  }
  .more-info {
    position: absolute; left: 39px; top: 952px;
    font-family: "Tinos", "Times New Roman", serif; font-weight: 700; color: var(--text-silver);
  }
  .more-info .label { font-size: 23px; letter-spacing: 1px; }
  .more-info .contact { font-size: 24px; margin-top: 16px; font-weight: 400; }
  .footer-band {
    position: absolute; left: 0; bottom: 0; width: 790px; height: 54px;
    background: linear-gradient(90deg, #0a1420 0%, #1d4a6e 45%, var(--light-blue) 100%);
  }
  .brand {
    position: absolute; left: 550px; top: 1091px; width: 222px; height: 57px;
    background: var(--brand-blue); display: flex; align-items: center; gap: 10px; padding: 0 10px;
  }
  .brand-square { width: 26px; height: 26px; background: var(--text-white); flex: none; }
  .brand-name { font-family: "Arimo", Arial, sans-serif; font-size: 19px; color: var(--text-white); }
</style>
</head>
<body>
  <main class="poster">
    <div class="hero-art" role="img" aria-label="Close-up of a vintage camera lens with copper dials and a strip of film, lit by blue studio light"></div>
    <div class="light-ray ray-one"></div>
    <div class="light-ray ray-two"></div>

    <p class="dates">Jan 1,2014 - June 30, 2014</p>

    <h1 class="headline">
      <span class="word-lights">Lights</span>
      <span class="word-camera">Camera</span>
      <span class="word-sold">Sold!</span>
    </h1>

    <h2 class="competition-title">FREE LISTING COMPETITION</h2>
    <div class="competition-rule"></div>

    <p class="pitch">
      WIN THE LISTING SERVICES OF AN EXCEPTIONAL,<br>
      PROGRESSIVE AND DYNAMIC REAL ESTATE TEAM<br>
      A WINNING VIDEO IS ALL<br>
      WE NEED.
    </p>

    <div class="more-info">
      <p class="label">MORE INFORMATION ON:</p>
      <p class="contact">FreeListing.KTHomesDirect.com</p>
      <p class="contact">email: FreeListing@KTHomesDirect.com</p>
    </div>

    <div class="footer-band"></div>
    <div class="brand">
      <span class="brand-square"></span>
      <span class="brand-name">KTHomesDirect.com</span>
    </div>
  </main>
</body>
</html>
```